Maple Sprout Menu (Vegetarian Restaurant Concept)

Maple Sprout is a new concept fast casual restaurant
renders are attached so you can see the style of restaurant
Maple Sproutt is a vibrant and modern Vegetarian fast casual restaurant concept that mixes fresh food, energy, great décor, and a comfortable, welcoming atmosphere to provide a memorable and all Vegetarian dining experience.
Our Mission is to be top of mind when consumers think Vegetarian food!
Target Market(s)
the menu is vegetarian and appeals to a broad demographic in USA
Colors
Designer to choose colors to be used in the design.
Requirements
Must have
- well colored and well laid out menu - should not be cartoonish
Nice to have
- For Phots please use the shots in this file:
- https://www.filecrate-example.com/sh/qwx7tr2bnm4kdle/BBBdK_pQrLmNZTHO5E_XYZ_Kb?dl=0
- note these are untouched and you are free to change as needed
Should not have
- Should not be cartoonish - nor kives, forks etc in the design

```html
<!DOCTYPE html>
<html lang="en">
<head>
<meta charset="utf-8">
<title>Maple Sprout Menu</title>
<link rel="stylesheet" href="https://fonts.googleapis.com/css2?family=Mukta:wght@400;500&display=swap">
<style>
  :root {
    --menu-green: #8cc443;
    --rule-white: #ffffff;
    --ink: #1c1c1c;
  }
  * { margin: 0; padding: 0; box-sizing: border-box; }
  html, body { width: 993px; height: 1200px; overflow: hidden; background: var(--menu-green); }
  .canvas { width: 993px; height: 1200px; position: relative; overflow: hidden; background: var(--menu-green); }
  .menu {
    position: absolute; left: 0; top: 0;
    width: 960px; height: 1160px;
    transform: scale(1.0344);
    transform-origin: 0 0;
    font-family: "Mukta", "Helvetica Neue", Arial, sans-serif;
    color: var(--ink);
  }
  .section-head {
    position: absolute; height: 61px;
    display: flex; align-items: center; justify-content: center;
  }
  .section-head::before, .section-head::after {
    content: ""; position: absolute; width: 360px; height: 40px;
    border-color: var(--rule-white); border-style: solid; border-width: 0;
  }
  .section-head::before { left: 0; top: 0; border-top-width: 3px; border-left-width: 3px; }
  .section-head::after { right: 0; bottom: 0; border-bottom-width: 3px; border-right-width: 3px; }
  .section-title { font-size: 20px; font-weight: 400; line-height: 24px; }

  .item { position: absolute; width: 360px; }
  .item-name { font-size: 18px; font-weight: 400; line-height: 24px; }
  .item-desc { font-size: 15px; line-height: 20.5px; margin-top: 10px; }
  .leaf {
    position: absolute; width: 24px; height: 28px;
    background: var(--rule-white);
    border-radius: 2px 100% 2px 100%;
    transform: rotate(-8deg);
  }
</style>
</head>
<body>
<div class="canvas">
<main class="menu">

  <!-- Salads -->
  <header class="section-head" style="left:40px;top:43px;width:403px;"><h2 class="section-title" style="margin-top:2px">Salads</h2></header>
  <span class="leaf" style="left:37px;top:124px"></span>
  <div class="item" style="left:83px;top:124px">
    <p class="item-name">Brussel Sprout Ceasar</p>
    <p class="item-desc">little gem romaine, toasted torn bread,<br>parmigiano reggiano</p>
  </div>
  <span class="leaf" style="left:37px;top:218px"></span>
  <div class="item" style="left:83px;top:217px">
    <p class="item-name">Heirloom Beet salad</p>
    <p class="item-desc">shaved chioggia beet, roasted golden beet,<br>red quinoa, little gem, arugula, lemon vinaigrette</p>
  </div>
  <span class="leaf" style="left:37px;top:318px"></span>
  <div class="item" style="left:83px;top:314px">
    <p class="item-name">Zesty Black Bean and Corn Salad<br>in lettuce cups</p>
    <p class="item-desc">black beans, avocado and roasted corn topped<br>with feta crumbles in butter lettuce</p>
  </div>
  <span class="leaf" style="left:37px;top:434px"></span>
  <div class="item" style="left:83px;top:431px">
    <p class="item-name">Green, Red and White</p>
    <p class="item-desc" style="margin-top:8px">spring leaves, cherry tomatoes, avocado,<br>roasted almond and goat cheese</p>
  </div>

  <!-- Burgers, Wraps & Sandwiches -->
  <header class="section-head" style="left:519px;top:43px;width:403px;"><h2 class="section-title" style="margin-top:-6px">Burgers, Wraps &amp; Sandwiches</h2></header>
  <span class="leaf" style="left:515px;top:130px"></span>
  <div class="item" style="left:561px;top:124px;width:380px">
    <p class="item-name">Sweet Potato, black bean veggie burgers<br>with cabbage - pepita slaw</p>
  </div>
  <span class="leaf" style="left:515px;top:198px"></span>
  <div class="item" style="left:561px;top:193px">
    <p class="item-name">Roasted Vejjie, Arugula and Hummus<br>Wraps</p>
  </div>
  <span class="leaf" style="left:515px;top:264px"></span>
  <div class="item" style="left:561px;top:260px">
    <p class="item-name">Garden Burger</p>
  </div>
  <span class="leaf" style="left:515px;top:313px"></span>
  <div class="item" style="left:561px;top:310px">
    <p class="item-name">Beans and Greens Quesadillas</p>
    <p class="item-desc" style="margin-top:6px">greens, Mexican cheese, beans and avocado,<br>with salsa</p>
  </div>
  <span class="leaf" style="left:515px;top:396px"></span>
  <div class="item" style="left:561px;top:393px">
    <p class="item-name">Vejjie Burrito</p>
    <p class="item-desc" style="margin-top:8px">greens, Mexican cheese, beans, brown rice,<br>roasted chili corn and avocado,<br>with ancho chili salsa, wheat tortilla</p>
  </div>

  <!-- Toasts -->
  <header class="section-head" style="left:40px;top:581px;width:403px;"><h2 class="section-title">Toasts</h2></header>
  <span class="leaf" style="left:33px;top:664px"></span>
  <div class="item" style="left:81px;top:663px">
    <p class="item-name">Everything Avocado toast</p>
    <p class="item-desc">avocado on whole grain toast with<br>our signature spice blend</p>
  </div>
  <span class="leaf" style="left:33px;top:755px"></span>
  <div class="item" style="left:81px;top:755px">
    <p class="item-name">Tomato &amp; Beet Bruschetta</p>
  </div>
  <span class="leaf" style="left:33px;top:796px"></span>
  <div class="item" style="left:81px;top:796px">
    <p class="item-name">Vegetable Melt on garlic Toast</p>
  </div>

  <!-- Bowls -->
  <header class="section-head" style="left:510px;top:581px;width:404px;"><h2 class="section-title">Bowls</h2></header>
  <span class="leaf" style="left:507px;top:661px"></span>
  <div class="item" style="left:555px;top:657px"><p class="item-name">Roasted vegetable, and spinach bowl</p></div>
  <span class="leaf" style="left:507px;top:705px"></span>
  <div class="item" style="left:555px;top:701px"><p class="item-name">Sugar Snap Pea and Carrot Soba Noodles</p></div>
  <span class="leaf" style="left:507px;top:748px"></span>
  <div class="item" style="left:555px;top:744px"><p class="item-name">Whole grain and vegetable buddha bowl</p></div>
  <span class="leaf" style="left:507px;top:790px"></span>
  <div class="item" style="left:555px;top:786px"><p class="item-name">Orange and Pistacio Quinoa</p></div>

  <!-- Dessert -->
  <header class="section-head" style="left:44px;top:897px;width:403px;"><h2 class="section-title" style="margin-top:-4px">Dessert</h2></header>
  <span class="leaf" style="left:41px;top:973px"></span>
  <div class="item" style="left:89px;top:975px"><p class="item-name">Strawberry Balsamic Ice Cream&nbsp; sundae</p></div>
  <span class="leaf" style="left:41px;top:1014px"></span>
  <div class="item" style="left:89px;top:1016px"><p class="item-name">Exotic fruit bowl</p></div>
  <span class="leaf" style="left:41px;top:1054px"></span>
  <div class="item" style="left:89px;top:1055px"><p class="item-name">White and dark oatmeal cookie</p></div>

  <!-- Soup -->
  <header class="section-head" style="left:510px;top:897px;width:403px;"><h2 class="section-title" style="margin-top:-4px">Soup</h2></header>
  <span class="leaf" style="left:507px;top:974px"></span>
  <div class="item" style="left:551px;top:972px"><p class="item-name">Black Bean Chowder</p></div>

</main>
</div>
</body>
</html>
```